Vale Tinto - Compotas / new label of jams and honey.

Send the old one to know the text you should have.
height of compote bottle - one 8cm x6,5cm ather 5cmx4,5cm
cherry; Apple; Blackberry; fig; orange; wait; blueberry.
height honey jar 13cm
diameter 6,5cm
Updates

the logo may have another color

Target Market(s)

Expensive and different product ...
people with money

Colors

Designer to choose colors to be used in the design.

Requirements
Must have
• image of fruit
• three languages: Portuguese, French and English.
Nice to have
• black and more colors
• see our facebook
• https://www.facebook.com/valetintodoces/

```html
<!DOCTYPE html>
<html lang="pt">
<head>
<meta charset="utf-8">
<title>Compota de Mirtilo – Vale Tinto</title>
<link rel="stylesheet" href="https://fonts.googleapis.com/css2?family=Caveat:wght@400;600&family=Montserrat:wght@400;600;700&display=swap">
<style>
  :root {
    --label-black: #000000;
    --paper: #ffffff;
    --ink-light: #ffffff;
    --ink-soft: #d9d9d9;
    --accent-purple: #5b4b9c;
    --berry-blue: #6f86ad;
    --berry-dark: #2f3e5e;
    --leaf-green: #5f9a45;
  }
  html, body {
    margin: 0;
    padding: 0;
    width: 1200px;
    height: 1200px;
    overflow: hidden;
    background: var(--paper);
  }
  .label {
    position: relative;
    width: 1200px;
    height: 1200px;
  }
  .label-art {
    position: absolute;
    inset: 0;
  }
  .ring-text {
    font-family: "Caveat", cursive;
    font-size: 15px;
    fill: var(--ink-light);
  }
  .maker {
    position: absolute;
    left: 450px;
    top: 628px;
    width: 300px;
    text-align: center;
    font-family: "Montserrat", sans-serif;
    color: var(--ink-light);
    line-height: 1.25;
  }
  .maker-lead { font-size: 10px; font-weight: 600; margin: 0; }
  .maker-trans { font-size: 7.5px; color: var(--ink-soft); margin: 0; }
  .maker-name { font-size: 12px; font-weight: 700; margin: 4px 0 1px; }
  .maker-address { font-size: 9.5px; font-weight: 600; margin: 0; }
  .net-weight {
    position: absolute;
    left: 500px;
    top: 736px;
    width: 200px;
    text-align: center;
    font-family: "Caveat", cursive;
    font-size: 30px;
    color: var(--ink-light);
    margin: 0;
  }
  .brand-mark {
    position: absolute;
    left: 571px;
    top: 557px;
    width: 58px;
    height: 58px;
    border-radius: 50%;
    background: var(--paper);
    display: flex;
    align-items: center;
    justify-content: center;
    font-family: "Montserrat", sans-serif;
    font-weight: 600;
    font-size: 9px;
    color: var(--label-black);
  }
  .product-title {
    position: absolute;
    left: 316px;
    top: 892px;
    width: 568px;
    text-align: center;
    font-family: "Caveat", cursive;
    font-weight: 600;
    font-size: 74px;
    line-height: 1;
    color: var(--ink-light);
    margin: 0;
  }
  .product-subtitle {
    position: absolute;
    left: 316px;
    top: 984px;
    width: 568px;
    text-align: center;
    font-family: "Caveat", cursive;
    font-size: 34px;
    color: var(--ink-light);
    margin: 0;
  }
</style>
</head>
<body>
<main class="label">
  <svg class="label-art" width="1200" height="1200" viewBox="0 0 1200 1200" xmlns="http://www.w3.org/2000/svg">
    <defs>
      <radialGradient id="berryTone" cx="50%" cy="55%" r="55%">
        <stop offset="0%" stop-color="#7e93b8"/>
        <stop offset="55%" stop-color="#5d7299"/>
        <stop offset="100%" stop-color="#6f9a55"/>
      </radialGradient>
      <radialGradient id="berrySmallTone" cx="50%" cy="60%" r="55%">
        <stop offset="0%" stop-color="#6f86ad"/>
        <stop offset="60%" stop-color="#4c5f85"/>
        <stop offset="100%" stop-color="#000000"/>
      </radialGradient>
      <path id="ingredientRing" d="M 420,352 a 180,180 0 1,1 360,0 a 180,180 0 1,1 -360,0"/>
    </defs>

    <!-- label die-cut -->
    <g class="label-shape" fill="var(--label-black)">
      <circle cx="600" cy="352" r="204"/>
      <rect x="498" y="480" width="204" height="380"/>
      <path d="M 316,1053 L 316,910 Q 316,846 380,846 L 820,846 Q 884,846 884,910 L 884,1053 Z"/>
    </g>

    <!-- fruit medallion -->
    <circle class="medallion" cx="600" cy="352" r="124" fill="var(--paper)" stroke="var(--accent-purple)" stroke-width="4"/>
    <ellipse role="img" aria-label="Photo of a cluster of blueberries with green leaves" cx="600" cy="352" rx="78" ry="90" fill="url(#berryTone)"/>

    <!-- ingredients ring -->
    <text class="ring-text">
      <textPath href="#ingredientRing" startOffset="30" textLength="1110" lengthAdjust="spacing">• Ingredientes: Mirtilo (60%), açúcar, água, sumo de limão e pectina • Ingredients: Blueberry (60%), sugar, water, lemon juice and pectin • Ingrédients: Myrtille (60%), sucre, eau, jus de citron et pectine</textPath>
    </text>

    <!-- small fruit image above title -->
    <ellipse role="img" aria-label="Photo of blueberries on a sprig with leaves" cx="600" cy="848" rx="58" ry="64" fill="url(#berrySmallTone)"/>

    <!-- purple underline stroke -->
    <path class="title-underline" d="M 348,974 L 852,972 L 852,979 L 348,981 Z" fill="var(--accent-purple)"/>
  </svg>

  <div class="brand-mark">Vale Tinto</div>

  <section class="maker">
    <p class="maker-lead">Produzido e embalado por:</p>
    <p class="maker-trans">Produced and packaged by:</p>
    <p class="maker-trans">Produit et emballé par:</p>
    <p class="maker-name">Vale Tinto</p>
    <p class="maker-address">Travessa das Amoras</p>
    <p class="maker-address">118 V. N. Gaia</p>
    <p class="maker-address">Portugal</p>
  </section>

  <p class="net-weight">220 gr.</p>

  <h1 class="product-title">Compota de Mirtilo</h1>
  <p class="product-subtitle">Blueberry Compote • Compote De Myrtilles</p>
</main>
</body>
</html>
```